Velcrest-Aura

Letter heads, business cards, packaging envelopes big and small, and stationery
We have logo design and trademarked approval, we would lie to
upload design to help create this project.
This product was created for my Mother a 4 time diganosed Cancer
Survivor, This product has patent pending and now will be offered to the general public as well.
We are looking foward to working with all of you as this product
and stationary will be viewed worldwide.
Thanks
The Kindale Family

Target Market(s)

all ages and worldwide

Industry/Entity Type

Business

Requirements
Must have
• Our Logo

```html
<!DOCTYPE html>
<html lang="en">
<head>
<meta charset="utf-8">
<title>Velcrest-Aura Stationery</title>
<link href="https://fonts.googleapis.com/css2?family=Rubik:wght@400;500;700&display=swap" rel="stylesheet">
<style>
  :root{
    --backdrop:#8e8e8e;
    --paper:#ededed;
    --navy:#1f3566;
    --red:#a3181d;
    --ink:#555;
    --window:#cfcfcf;
  }
  *{box-sizing:border-box;margin:0;padding:0}
  html,body{width:1200px;height:675px;overflow:hidden}
  body{background:var(--backdrop);font-family:"Rubik",Arial,sans-serif;position:relative}
  .sheet{position:absolute;background:var(--paper);box-shadow:0 3px 10px rgba(0,0,0,.25);overflow:hidden}
  .band{position:absolute;left:0;right:0;bottom:0;background:var(--navy)}
  .brand{position:absolute;line-height:1;white-space:nowrap}
  .brand-name{font-weight:700;color:var(--navy);display:flex;align-items:center;gap:.3em}
  .brand-dot{display:inline-block;width:.8em;height:.8em;border-radius:50%;background:var(--red)}
  .brand-tagline{font-weight:500;color:var(--red);margin-top:.3em;padding-left:1.1em}
  .contact{position:absolute;list-style:none;color:var(--ink)}
  .contact li{display:flex;align-items:center;gap:5px;white-space:nowrap}
  .contact svg{fill:var(--red);flex:none}

  .letterhead{left:40px;top:80px;width:380px;height:480px}
  .letterhead .brand{left:24px;top:30px;font-size:18px}
  .letterhead .brand-tagline{font-size:8.5px}
  .letterhead .contact{right:22px;top:28px;font-size:7px;line-height:12px}
  .letterhead .band{height:14px}

  .envelope-window{left:460px;top:60px;width:470px;height:230px}
  .envelope-window .brand{left:30px;top:30px;font-size:20px}
  .envelope-window .brand-tagline{font-size:9px}
  .envelope-window .address-window{position:absolute;left:40px;top:110px;width:200px;height:70px;background:var(--window);border-radius:4px}
  .envelope-window .band{height:12px}

  .envelope-back{left:460px;top:330px;width:470px;height:230px}
  .envelope-back .flap{position:absolute;left:0;right:0;top:0;height:22px;background:var(--red)}
  .envelope-back .brand{left:30px;top:60px;font-size:20px}
  .envelope-back .brand-tagline{font-size:9px}
  .envelope-back .contact{left:30px;top:135px;font-size:7px;line-height:12px}
  .envelope-back .band{height:12px}

  .card-front{left:975px;top:180px;width:190px;height:110px}
  .card-front .brand{left:16px;top:32px;font-size:17px}
  .card-front .brand-tagline{font-size:7.5px}
  .card-front .band{height:7px}

  .card-back{left:975px;top:330px;width:190px;height:110px}
  .card-back .brand{left:12px;top:12px;font-size:12px}
  .card-back .brand-tagline{font-size:5.5px}
  .card-back .holder{position:absolute;left:12px;top:44px;color:var(--red);font-size:9px}
  .card-back .holder-role{color:var(--ink);font-size:6px;margin-top:1px}
  .card-back .contact{left:12px;top:66px;font-size:5.5px;line-height:8px}
  .card-back .band{height:6px}
</style>
</head>
<body>
<svg width="0" height="0" style="position:absolute" aria-hidden="true">
  <symbol id="icon-pin" viewBox="0 0 10 10"><path d="M5 0a3.5 3.5 0 0 0-3.5 3.5C1.5 6 5 10 5 10s3.5-4 3.5-6.5A3.5 3.5 0 0 0 5 0zm0 5a1.5 1.5 0 1 1 0-3 1.5 1.5 0 0 1 0 3z"/></symbol>
  <symbol id="icon-phone" viewBox="0 0 10 10"><path d="M2 0h2l1 2.5-1.3 1a6 6 0 0 0 2.8 2.8l1-1.3L10 6v2a2 2 0 0 1-2 2C3.6 10 0 6.4 0 2a2 2 0 0 1 2-2z"/></symbol>
  <symbol id="icon-mail" viewBox="0 0 10 10"><path d="M0 2h10v6H0zM1 3v.3l4 2.5 4-2.5V3z"/></symbol>
  <symbol id="icon-globe" viewBox="0 0 10 10"><circle cx="5" cy="5" r="4.2" fill="none" stroke="currentColor"/><path d="M.8 5h8.4M5 .8v8.4" stroke="currentColor" stroke-width=".8" fill="none"/></symbol>
</svg>

<section class="sheet letterhead">
  <div class="brand">
    <div class="brand-name"><span class="brand-dot"></span>Velcrest-Aura</div>
    <div class="brand-tagline">Calm Comfort For Every Day</div>
  </div>
  <ul class="contact">
    <li><svg width="7" height="7"><use href="#icon-pin"/></svg>2864 Harbor Lane, Stone Ridge 20410</li>
    <li><svg width="7" height="7"><use href="#icon-phone"/></svg>555 010 2222</li>
    <li><svg width="7" height="7"><use href="#icon-mail"/></svg>hello@velcrestaura.com</li>
    <li><svg width="7" height="7" style="color:var(--red)"><use href="#icon-globe"/></svg>www.velcrestaura.com</li>
  </ul>
  <div class="band"></div>
</section>

<section class="sheet envelope-window">
  <div class="brand">
    <div class="brand-name"><span class="brand-dot"></span>Velcrest-Aura</div>
    <div class="brand-tagline">Calm Comfort For Every Day</div>
  </div>
  <div class="address-window"></div>
  <div class="band"></div>
</section>

<section class="sheet envelope-back">
  <div class="flap"></div>
  <div class="brand">
    <div class="brand-name"><span class="brand-dot"></span>Velcrest-Aura</div>
    <div class="brand-tagline">Calm Comfort For Every Day</div>
  </div>
  <ul class="contact">
    <li><svg width="7" height="7"><use href="#icon-pin"/></svg>2864 Harbor Lane, Stone Ridge 20410</li>
    <li><svg width="7" height="7"><use href="#icon-phone"/></svg>555 010 2222</li>
    <li><svg width="7" height="7"><use href="#icon-mail"/></svg>hello@velcrestaura.com</li>
    <li><svg width="7" height="7" style="color:var(--red)"><use href="#icon-globe"/></svg>www.velcrestaura.com</li>
  </ul>
  <div class="band"></div>
</section>

<section class="sheet card-front">
  <div class="brand">
    <div class="brand-name"><span class="brand-dot"></span>Velcrest-Aura</div>
    <div class="brand-tagline">Calm Comfort For Every Day</div>
  </div>
  <div class="band"></div>
</section>

<section class="sheet card-back">
  <div class="brand">
    <div class="brand-name"><span class="brand-dot"></span>Velcrest-Aura</div>
    <div class="brand-tagline">Calm Comfort For Every Day</div>
  </div>
  <div class="holder">Dana Morrow<div class="holder-role">Manager</div></div>
  <ul class="contact">
    <li><svg width="5" height="5"><use href="#icon-pin"/></svg>2864 Harbor Lane, Stone Ridge 20410</li>
    <li><svg width="5" height="5"><use href="#icon-phone"/></svg>555 010 2222</li>
    <li><svg width="5" height="5"><use href="#icon-mail"/></svg>hello@velcrestaura.com</li>
    <li><svg width="5" height="5" style="color:var(--red)"><use href="#icon-globe"/></svg>www.velcrestaura.com</li>
  </ul>
  <div class="band"></div>
</section>
</body>
</html>
```